Nine Dawns and Four Decades Book Cover Design

I need a book cover design for a book that I am writing, called "Nine Dawns and Four Decades: The Dash and Endurance Path of Reaching Peak Results".

I have attached the Table of Contents and the first Introduction Chapter of the book, to provide more context on what the book is about.

The stories in the book primarily rely on my experience of running SkyVela Q, a long-haul low-cost airline. I use "sprint and marathon" because I'm a marathon runner and ironman triathlete, and its part of my identity.

I would love a design that captures a stylized combination of an aircraft taking off, and a person running. I have attached a photo of an SkyVela Q Corvane K740 aircraft (its different from SkyVela planes because of the "X" paint strokes on the tail of the plane. Ideally, if a stylized version of the X appears on the tail, that would be great, but without the "SkyVela" text.

Generally, the cover should convey "speed", and "curiosity".

Target Market(s)

Business Book Readers in Asia

Font styles to use
Sans Serif

Colors

Designer to choose colors to be used in the design.

Requirements
Must have
• Text in the Cover from the attached file
Nice to have
• Aircraft taking off and someone running
Should not have
• "SkyVela" name/text.

```html
<!DOCTYPE html>
<html lang="en">
<head>
<meta charset="utf-8">
<title>Nine Dawns and Four Decades — Book Cover</title>
<link rel="stylesheet" href="https://fonts.googleapis.com/css2?family=Teko:wght@400;500;600&display=swap">
<style>
  :root {
    --stage: #d9d9d9;
    --title-red: #e2474d;
    --title-red-deep: #d23a40;
    --light-text: #f1ece0;
    --sky-top: #e9e9e7;
    --sky-mid: #f4f1e6;
    --glow: #e9dca0;
    --field: #a2a063;
    --road-light: #b8b2a3;
    --road-dark: #3f3c37;
  }
  html, body {
    margin: 0;
    padding: 0;
    width: 1200px;
    height: 1200px;
    overflow: hidden;
    background: var(--stage);
  }
  .book-cover {
    position: absolute;
    left: 232px;
    top: 50px;
    width: 736px;
    height: 1100px;
    overflow: hidden;
    font-family: "Teko", "Arial Narrow", sans-serif;
  }
  .cover-photo {
    position: absolute;
    inset: 0;
    width: 100%;
    height: 100%;
  }
  .title-block {
    position: absolute;
    left: 0;
    width: 528px;
    text-align: center;
    color: var(--title-red);
    text-transform: uppercase;
  }
  .title-big {
    display: block;
    font-weight: 600;
    font-size: 240px;
    line-height: 0.8;
    letter-spacing: -2px;
  }
  .title-small {
    display: block;
    font-weight: 500;
    font-size: 52px;
    line-height: 0.9;
    color: var(--title-red-deep);
  }
  .title-line-1 { top: 250px; }
  .title-line-2 { top: 482px; }
  .title-line-3 { top: 540px; }
  .title-line-4 { top: 760px; }
  .subtitle {
    position: absolute;
    left: 0;
    width: 528px;
    top: 846px;
    margin: 0;
    text-align: center;
    color: var(--light-text);
    font-weight: 400;
    font-size: 36px;
    line-height: 1.1;
    text-transform: uppercase;
  }
  .author {
    position: absolute;
    left: 0;
    width: 528px;
    top: 990px;
    margin: 0;
    text-align: center;
    color: var(--light-text);
    font-weight: 500;
    font-size: 66px;
    line-height: 1;
    letter-spacing: 1px;
    word-spacing: 14px;
    text-transform: uppercase;
  }
</style>
</head>
<body>
  <main class="book-cover">
    <svg class="cover-photo" viewBox="0 0 736 1100" preserveAspectRatio="none" role="img"
         aria-label="Photo of a runner seen from behind on a long open road, with a red-and-white jet climbing into a hazy bright sky at upper left">
      <defs>
        <linearGradient id="scene" x1="0" y1="0" x2="0" y2="1">
          <stop offset="0" stop-color="var(--sky-top)"/>
          <stop offset="0.45" stop-color="var(--sky-mid)"/>
          <stop offset="0.52" stop-color="var(--glow)"/>
          <stop offset="0.56" stop-color="var(--field)"/>
          <stop offset="0.62" stop-color="var(--road-light)"/>
          <stop offset="1" stop-color="var(--road-dark)"/>
        </linearGradient>
        <radialGradient id="sun" cx="0.6" cy="0.5" r="0.5">
          <stop offset="0" stop-color="#fff6cf" stop-opacity="0.7"/>
          <stop offset="1" stop-color="#fff6cf" stop-opacity="0"/>
        </radialGradient>
      </defs>
      <rect width="736" height="1100" fill="url(#scene)"/>
      <rect width="736" height="1100" fill="url(#sun)"/>
    </svg>

    <h1 class="title">
      <span class="title-block title-big title-line-1">Nine</span>
      <span class="title-block title-small title-line-2">Dawns &amp;</span>
      <span class="title-block title-big title-line-3">Four</span>
      <span class="title-block title-small title-line-4">Decades</span>
    </h1>

    <p class="subtitle">The Dash and Endurance Path<br>of Reaching Peak Results</p>

    <p class="author">Arvin Tessaly-Roan</p>
  </main>
</body>
</html>
```